Business Card

Can you please copy the format provided for the business cards.
Can the logo be in the colours of the last file as specified.

Can the text please be in grey

• Navy Blue: #00457C
• Grey Text: #555555
• Orange Text: #FDBF29

The names on the business card will be

Dorian Pike
0455 718 302
dorian.pike@tallowridgeleasing.example.au

Lvl 7, 14 Harlow Pde
Merrivale QLD 4388
PO Box 3412
Sunhaven MC QLD 9812
P: 1300 742 619
F: 1300 742 638
www.tallowridgeleasing.example.au

And

Leon Whitcombe
0467 590 148
leon.whitcombe@tallowridgeleasing.example.au

Lvl 7, 14 Harlow Pde
Merrivale QLD 4388
PO Box 3412
Sunhaven MC QLD 9812
P: 1300 742 619
F: 1300 743 905

```html
<!DOCTYPE html>
<html lang="en">
<head>
<meta charset="utf-8">
<title>Tallowridge Leasing – Business Card</title>
<link rel="stylesheet" href="https://fonts.googleapis.com/css2?family=Source+Sans+3:wght@400&family=Varela+Round&display=swap">
<style>
  :root {
    --navy: #0e4a7e;
    --grey-text: #555555;
    --accent: #fdbf29;
    --white: #ffffff;
    --backdrop: #5e5e5e;
  }
  * { box-sizing: border-box; margin: 0; padding: 0; }
  html, body {
    width: 1200px;
    height: 1000px;
    overflow: hidden;
  }
  body {
    background: var(--backdrop);
    position: relative;
    font-family: "Varela Round", sans-serif;
  }
  .card {
    position: absolute;
    top: 347px;
    width: 502px;
    height: 306px;
    box-shadow: 0 3px 8px rgba(0, 0, 0, 0.35);
    overflow: hidden;
  }

  /* Front – personal side */
  .card-front {
    left: 67px;
    background: var(--navy);
    color: var(--white);
  }
  .card-front .person-name {
    position: absolute;
    top: 22px;
    right: 46px;
    font-family: "Source Sans 3", sans-serif;
    font-weight: 400;
    font-size: 23px;
    letter-spacing: 0.2px;
  }
  .card-front .person-contact {
    position: absolute;
    left: 41px;
    top: 234px;
    font-size: 14px;
    line-height: 22px;
    letter-spacing: 0.2px;
  }

  /* Back – company side */
  .card-back {
    left: 630px;
    background: var(--white);
  }
  .brand-panel {
    height: 191px;
    display: flex;
    align-items: center;
    justify-content: center;
    gap: 18px;
  }
  .brand-square {
    width: 44px;
    height: 44px;
    background: var(--navy);
  }
  .brand-name {
    font-size: 34px;
    font-weight: 400;
    color: var(--grey-text);
    letter-spacing: 0.5px;
  }
  .company-details {
    height: 115px;
    background: var(--navy);
    color: var(--white);
    text-align: center;
    padding-top: 12px;
  }
  .company-details p {
    font-size: 13.5px;
    line-height: 21.5px;
  }
  .company-details .website {
    font-size: 15.5px;
    margin-top: 3px;
  }
</style>
</head>
<body>
  <section class="card card-front" aria-label="Business card front">
    <h1 class="person-name">Dorian Pike</h1>
    <div class="person-contact">
      <p class="phone">0455 718 302</p>
      <p class="email">dorian.pike@tallowridgeleasing.example.au</p>
    </div>
  </section>

  <section class="card card-back" aria-label="Business card back">
    <div class="brand-panel">
      <span class="brand-square"></span>
      <span class="brand-name">Tallowridge Leasing</span>
    </div>
    <div class="company-details">
      <p>Lvl 7, 14 Harlow Pde, Merrivale QLD 4388</p>
      <p>PO Box 3412, Sunhaven MC QLD 9812</p>
      <p>P: 1300 742 619, F: 1300 742 638</p>
      <p class="website">www.tallowridgeleasing.example.au</p>
    </div>
  </section>
</body>
</html>
```